Business Card Design Project

We are a consulting company which works with tourism operators and attractions, wineries, heritage sites, National and conservation parks etc to help them identify their 'Point of Difference' and then deliver an exceptional tourism visitor experience.
We specialise in: Operator training, Site interpretation, Product and experience development, Planning and analysis.
We have a tag line of "Telling your story - really well."
The company name is MornVoice and the logo is this word with the 'Morn' in black and the 'Voice' in orange - but this can be changed. The 'a' is a speech bubble. A lot of what we do involves talking!
The design should communicate that we can make a big difference to the range and quality of experiences that visitors get at your site.
Updates

I put the wrong telephone number in my brief. My apologies.

It should be +61 0487 555 913

Target Market(s)

tourism busineses, wineries and cellar doors, heritage sites, environment managers, Government agencies & private companies

Industry/Entity Type

Tourism

Requirements
Must have
• Name: Ruth Pellow
Title: Emeritus Professor
Qualifications: BSc(Hons), PhD
Role: Director
Address: PO Box 317, Brighton, South Australia 5048
Phone: (+61) 0487 555 913
Email: ruth@mornvoice-example.com.au
www.mornvoice-example.com.au
ABN 514 072 389 16

Operator Training, Site Interpretation, Product and Experience Development, Planning and Analysis.
Nice to have
• Awards:
Winner 2011 Coastline Visitor Honours – Kestrel College - Tourism Education and Training
Winner 2009 Coastline Visitor Honours - Outstanding Contribution by an Individual
Winner 2009 Gulfside Citizen Medal - Tourism Award
Should not have
• No 'shadows' to company name/logo please.
No black reverse side of card

```html
<!DOCTYPE html>
<html lang="en">
<head>
<meta charset="utf-8">
<title>MornVoice Consulting – Business Card</title>
<link rel="stylesheet" href="https://fonts.googleapis.com/css2?family=Open+Sans:wght@400;600;700&family=Arimo:wght@400&display=swap">
<style>
  :root {
    --backdrop: #4b4b4d;
    --card: #f4f4f4;
    --ink: #1b1b1b;
    --teal: #149b86;
    --grey-text: #5c5c5c;
    --grey-bar: #9a9a9a;
    --grey-band: #b9b9b9;
    --white: #ffffff;
  }
  * { box-sizing: border-box; margin: 0; padding: 0; }
  html, body {
    width: 1200px; height: 1000px; overflow: hidden;
    background: var(--backdrop);
    font-family: "Open Sans", sans-serif;
    color: var(--ink);
  }
  .canvas { position: relative; width: 1200px; height: 1000px; }

  .card {
    position: absolute;
    width: 528px; height: 300px;
    background: var(--card);
    border-radius: 14px;
    overflow: hidden;
  }
  .card--front { left: 207px; top: 165px; }
  .card--back  { left: 472px; top: 534px; }

  /* Wordmark */
  .wordmark {
    position: absolute;
    font-family: "Open Sans", sans-serif;
    font-weight: 700;
    color: var(--teal);
    line-height: 1;
    white-space: nowrap;
  }
  .wordmark__name { font-size: 42px; letter-spacing: -1px; display: block; }
  .wordmark__sub {
    display: block; text-align: right;
    font-size: 13px; letter-spacing: 2.5px; margin-top: 4px;
  }
  .card--front .wordmark { left: 28px; top: 64px; }
  .card--back .wordmark  { right: 38px; top: 68px; }

  /* Front: contact block */
  .contact {
    position: absolute; right: 40px; text-align: right;
    font-size: 11.5px; line-height: 16px;
  }
  .contact__name { font-size: 18px; font-weight: 700; line-height: 22px; letter-spacing: 0.3px; }
  .contact__title { font-size: 13px; line-height: 18px; }
  .contact__quals { font-size: 11px; color: var(--teal); line-height: 16px; }
  .contact__label { color: var(--teal); font-weight: 700; }
  .contact--identity { top: 60px; }
  .contact--reach { top: 172px; }
  .contact--post { top: 220px; }
  .contact--abn { top: 264px; color: var(--grey-text); font-size: 11px; }

  .side-tab {
    position: absolute; right: 0; top: 61px;
    width: 10px; height: 50px; background: var(--teal);
  }
  .web {
    position: absolute; left: 127px; top: 263px;
    font-size: 13px; color: var(--ink);
  }
  .web__brand { color: var(--teal); font-weight: 600; }
  .foot-bar {
    position: absolute; left: 127px; bottom: 0;
    width: 106px; height: 10px; background: var(--grey-bar);
  }

  /* Back: services */
  .services {
    position: absolute; left: 34px; top: 38px;
    list-style: none;
    font-family: "Arimo", sans-serif; font-size: 12.5px;
    text-transform: uppercase; line-height: 29px;
  }
  .services__item { position: relative; padding-left: 28px; }
  .services__item svg { position: absolute; left: 0; top: 7px; }
  .services__item--cont { padding-left: 28px; }

  .tagline {
    position: absolute; right: 38px; top: 158px;
    font-family: "Arimo", sans-serif; font-size: 12.5px; color: #333;
  }

  .grey-band {
    position: absolute; left: 0; top: 212px;
    width: 100%; height: 14px; background: var(--grey-band);
  }
  .awards {
    position: absolute; left: 0; top: 228px;
    width: 100%; height: 72px; background: var(--teal);
    color: var(--white);
  }
  .awards__badge { position: absolute; left: 14px; top: -10px; }
  .awards__list {
    list-style: none; position: absolute; left: 81px; top: 13px;
    font-size: 9.8px; letter-spacing: -0.1px; line-height: 17px; white-space: nowrap;
  }
  .awards__list strong { font-weight: 700; }
</style>
</head>
<body>
<main class="canvas">

  <section class="card card--front" aria-label="Business card front">
    <div class="wordmark">
      <span class="wordmark__name">MornVoice</span>
      <span class="wordmark__sub">CONSULTING</span>
    </div>

    <div class="contact contact--identity">
      <p class="contact__name">RUTH PELLOW</p>
      <p class="contact__title">Emeritus Professor</p>
      <p class="contact__quals">Qualifications: BSc(Hons), PhD</p>
    </div>
    <div class="side-tab"></div>

    <div class="contact contact--reach">
      <p><span class="contact__label">Phone:</span> +61 0487 555 913</p>
      <p><span class="contact__label">Email:</span> ruth@mornvoice-example.com.au</p>
    </div>
    <div class="contact contact--post">
      <p>PO Box 317, Brighton</p>
      <p>South Australia 5048</p>
    </div>
    <p class="contact contact--abn">ABN 514 072 389 16</p>

    <p class="web">www.<span class="web__brand">mornvoice</span>-example.com.au</p>
    <div class="foot-bar"></div>
  </section>

  <section class="card card--back" aria-label="Business card back">
    <ul class="services">
      <li class="services__item"><svg width="16" height="16" viewBox="0 0 16 16"><path d="M3 1h10a2 2 0 0 1 2 2v6a2 2 0 0 1-2 2H8l-2 4-1-4H3a2 2 0 0 1-2-2V3a2 2 0 0 1 2-2z" fill="#149b86"/></svg>Operator Training</li>
      <li class="services__item"><svg width="16" height="16" viewBox="0 0 16 16"><path d="M3 1h10a2 2 0 0 1 2 2v6a2 2 0 0 1-2 2H8l-2 4-1-4H3a2 2 0 0 1-2-2V3a2 2 0 0 1 2-2z" fill="#149b86"/></svg>Site Interpretation</li>
      <li class="services__item"><svg width="16" height="16" viewBox="0 0 16 16"><path d="M3 1h10a2 2 0 0 1 2 2v6a2 2 0 0 1-2 2H8l-2 4-1-4H3a2 2 0 0 1-2-2V3a2 2 0 0 1 2-2z" fill="#149b86"/></svg>Product and Experience</li>
      <li class="services__item services__item--cont">Development</li>
      <li class="services__item"><svg width="16" height="16" viewBox="0 0 16 16"><path d="M3 1h10a2 2 0 0 1 2 2v6a2 2 0 0 1-2 2H8l-2 4-1-4H3a2 2 0 0 1-2-2V3a2 2 0 0 1 2-2z" fill="#149b86"/></svg>Planning and Analysis</li>
    </ul>

    <div class="wordmark">
      <span class="wordmark__name">MornVoice</span>
      <span class="wordmark__sub">CONSULTING</span>
    </div>
    <p class="tagline">Telling your story - really well.</p>

    <div class="grey-band"></div>
    <div class="awards">
      <svg class="awards__badge" width="52" height="84" viewBox="0 0 52 84" aria-hidden="true">
        <path d="M14 40 L6 78 L16 70 L22 80 L28 44 Z M38 40 L46 78 L36 70 L30 80 L24 44 Z" fill="#e6e6e6"/>
        <circle cx="26" cy="28" r="25" fill="#9c9c9c"/>
        <circle cx="26" cy="28" r="19" fill="#b5b5b5"/>
      </svg>
      <ul class="awards__list">
        <li><strong>WINNER</strong> 2011 Coastline Visitor Honours – Kestrel College – Tourism Education and Training</li>
        <li><strong>WINNER</strong> 2009 Coastline Visitor Honours – Outstanding Contribution by an Individual</li>
        <li><strong>WINNER</strong> 2009 Gulfside Citizen Medal – Tourism Award</li>
      </ul>
    </div>
  </section>

</main>
</body>
</html>
```